Stock certificate

We need a stock certificate with a modern design aligned with our company background (Consulting & IT-Services Company with innovation drive).
The certificate should include our logo and should have some space to insert our dedicated text (value, issuer, etc.).
Format should be A4 landscape. The page must be workable, meaning that the background of the certificate can be fixed (kind of master), but the front where the text shall be written must be flexible. PPT-format could make it for example.
Tarsel font style desired.
Required text areas are shown in the uploaded example.
Tarsel font style would be great.
It Company

```html
<!DOCTYPE html>
<html lang="de">
<head>
<meta charset="utf-8">
<title>Aktienzertifikat – Veranth</title>
<link rel="stylesheet" href="https://fonts.googleapis.com/css2?family=Roboto:wght@100;300;400;700&display=swap">
<style>
  :root {
    --blue-deep: #0f4f8c;
    --blue-mid: #2f7fc4;
    --blue-soft: #9cc6ea;
    --blue-pale: #e6f0f9;
    --paper: #ffffff;
    --panel: rgba(255, 255, 255, 0.55);
    --panel-faint: rgba(255, 255, 255, 0.45);
    --ink: #1e2328;
    --ink-muted: #7d8894;
    --rule: #5c7fa6;
    --logo-ink: #2f3439;
  }
  * { box-sizing: border-box; margin: 0; padding: 0; }
  html, body { width: 1200px; height: 900px; overflow: hidden; }
  body { font-family: "Roboto", "Helvetica Neue", Arial, sans-serif; background: var(--paper); }

  .certificate { position: relative; width: 1200px; height: 900px; overflow: hidden; }

  .certificate__backdrop {
    position: absolute; inset: 0;
    background:
      radial-gradient(ellipse 70% 45% at 20% 10%, rgba(255,255,255,0.35), transparent 70%),
      linear-gradient(160deg, var(--blue-mid) 0%, var(--blue-deep) 28%, var(--blue-soft) 52%, var(--blue-pale) 72%, var(--paper) 90%);
  }

  .certificate__title {
    position: absolute; left: 86px; top: 24px; width: 1036px;
    font-weight: 100; font-size: 128px; line-height: 1;
    letter-spacing: -5.5px; color: rgba(255,255,255,0.55);
    white-space: nowrap; text-align: center;
  }

  .panel { position: absolute; left: 85px; width: 1035px; background: var(--panel); }
  .panel--parties { top: 198px; height: 166px; }
  .panel--description { top: 380px; height: 208px; background: var(--panel-faint); }

  .field { position: absolute; border-bottom: 1px solid var(--rule); }
  .field__label { display: block; font-weight: 300; }
  .field--meta { top: 20px; height: 24px; }
  .field--meta .field__label { font-size: 17px; color: var(--ink-muted); }
  .field--party { top: 73px; height: 87px; }
  .field--party .field__label { font-size: 21px; color: var(--ink); }
  .field--left { left: 11px; width: 461px; }
  .field--right { left: 556px; width: 461px; }

  .description__heading {
    margin-top: 11px; text-align: center;
    font-size: 20px; font-weight: 300; color: var(--ink);
  }
  .description__body {
    margin: 14px 14px 0; text-align: center;
    font-size: 14.8px; line-height: 17.8px; font-weight: 300; color: var(--ink-muted);
  }

  .brand {
    position: absolute; left: 822px; top: 668px; width: 296px; height: 62px;
    background: var(--paper);
    display: flex; align-items: center; justify-content: center;
  }
  .brand__name { font-size: 56px; font-weight: 700; color: var(--logo-ink); letter-spacing: 1px; line-height: 1; }

  .signatures {
    position: absolute; left: 70px; top: 752px; width: 1050px; height: 148px;
    background: rgba(255,255,255,0.5);
  }
  .signature { position: absolute; top: 28px; width: 285px; color: var(--ink-muted); font-weight: 300; font-size: 17px; }
  .signature__name { display: block; padding-bottom: 19px; border-bottom: 1px solid var(--rule); line-height: 20px; }
  .signature__role { display: block; margin-top: 7px; line-height: 20px; }
  .signature:nth-child(1) { left: 6px; }
  .signature:nth-child(2) { left: 385px; }
  .signature:nth-child(3) { left: 745px; }
</style>
</head>
<body>
<main class="certificate">
  <div class="certificate__backdrop" role="img" aria-label="Abstract flowing blue wave background with fine line mesh, fading to white at the bottom"></div>

  <h1 class="certificate__title">AKTIENZERTIFIKAT</h1>

  <section class="panel panel--parties">
    <div class="field field--meta field--left"><span class="field__label">No of certificate: 00000000</span></div>
    <div class="field field--meta field--right"><span class="field__label">Location, date</span></div>
    <div class="field field--party field--left"><span class="field__label">The Shareholder</span></div>
    <div class="field field--party field--right"><span class="field__label">Company</span></div>
  </section>

  <section class="panel panel--description">
    <h2 class="description__heading">Description</h2>
    <p class="description__body">Lorem ipsum dolor sit amet, consectetur adipiscing elit. Donec scelerisque ligula mi, ac consequat risus iaculis et. Vivamus ullamcorper mauris auctor semper commodo. Integer volutpat massa eget sapien placerat fringilla. Curabitur eu volutpat tortor. Ut viverra dolor sapien, sed hendrerit ipsum ultricies eu. Pellentesque condimentum scelerisque velit at viverra. Sed auctor pulvinar eros ut sollicitudin. Donec posuere eget turpis congue tempus. Nulla facilisis, augue non eleifend ultrices, nibh leo lacinia elit, eget ultricies leo arcu quis lacus. Praesent laoreet vehicula massa pulvinar tincidunt. Curabitur sagittis, lorem sit amet sollicitudin mattis, est mi scelerisque sapien, et tempus purus arcu non urna. Fusce sollicitudin odio nec adipiscing aliquet. Nullam rhoncus lorem non commodo egestas. Morbi sit amet tincidunt turpis. Nullam a sapien luctus, vulputate metus ut, gravida velit.</p>
  </section>

  <div class="brand">
    <span class="brand__name">Veranth</span>
  </div>

  <footer class="signatures">
    <div class="signature"><span class="signature__name">Name</span><span class="signature__role">Member of the board</span></div>
    <div class="signature"><span class="signature__name">Name</span><span class="signature__role">Member of the board</span></div>
    <div class="signature"><span class="signature__name">Name</span><span class="signature__role">Member of the board</span></div>
  </footer>
</main>
</body>
</html>
```